Business Card for Marriage Commissioner

I am a marriage commissioner in the province of Alberta, meaning that I perform civil unions here. I have been trying to think of a unique design for my business card, something a bit different. A lot of "unique" designs seem to incorporate unique cuts or "some assembly required" or printed on plastic or meat. I would like my design to be a full colour card that is a typical business card size.

The information on the card should have:
Lou Varnik
my occupation: Marriage Commissioner
my website: www.louvarnik.ca
my e-mail: lou@louvarnik.ca
my phone: 780-418-2964

I originally submitted a design to the printer that had a screen capture of a findly search window, with my name and occupation in the text box. And underneath that, my phone number. Nothing else. They indicated they could not print this because it was a copyright violation.

One option on the design is I am a retired chemist-so a chemistry themed card would also be of interest, as long as it isn't a "Rusted Tide" theme, as I have that on my other business cards already...

I would prefer a single sided card, but I am open to a double sided card if it is clever!

I would also prefer not to have pictures of male and female couples as in my position I will also marry same sex couples. Same thing for male/female symbols. Someone has submitted two graduated cylinders in love, which is very clever, and gets around this male/female type.

Thanks for your help and interest.

Target Market(s)

Young couples.

Industry/Entity Type

Plastic

Requirements
Nice to have
• chemistry ideas!
Should not have
• Male/female pictures, male/female symbols.
No QR codes.
No transparent designs, will go on paper stock.

```html
<!DOCTYPE html>
<html lang="en">
<head>
<meta charset="utf-8">
<title>Lou Varnik – Marriage Commissioner</title>
<link rel="stylesheet" href="https://fonts.googleapis.com/css2?family=Yellowtail&family=Dancing+Script:wght@700&family=Open+Sans:wght@400;600&display=swap">
<style>
  :root {
    --page: #e9e7e4;
    --card-light: #a9a9a9;
    --card-mid: #858585;
    --card-dark: #5a5a5a;
    --ornament: #6e6e6e;
    --ink: #ffffff;
    --name-ink: #141414;
    --rule: #e0e0e0;
    --icon-bg: #262626;
    --frame: #d4d4d4;
    --photo-green: #6f8a4e;
    --photo-skin: #cfb4a0;
    --photo-dark: #2f3036;
  }
  * { margin: 0; padding: 0; box-sizing: border-box; }
  html, body { width: 1200px; height: 1058px; overflow: hidden; background: var(--page); }
  .canvas { position: relative; width: 1200px; height: 1058px; }
  .card {
    position: absolute; left: 100px; top: 243px; width: 1000px; height: 572px;
    border-radius: 6px; overflow: hidden;
    background: radial-gradient(ellipse at 68% 45%, var(--card-light) 0%, var(--card-mid) 55%, var(--card-dark) 100%);
    box-shadow: 0 10px 30px rgba(0,0,0,.25);
  }
  .card-art { position: absolute; inset: 0; }
  .identity { position: absolute; left: 540px; top: 112px; width: 420px; }
  .rule { height: 2px; background: var(--rule); opacity: .85; }
  .name {
    font-family: "Yellowtail", "Dancing Script", cursive; font-size: 72px; line-height: 1.05;
    color: var(--name-ink); margin: 14px 0 0 8px;
    text-shadow: 0 0 2px rgba(255,255,255,.7);
  }
  .occupation {
    font-family: "Open Sans", sans-serif; font-weight: 400; font-size: 25px;
    color: var(--ink); margin: 0 0 10px 64px;
  }
  .contacts { list-style: none; position: absolute; left: 548px; top: 282px; }
  .contact {
    display: flex; align-items: center; gap: 16px; height: 54px;
    font-family: "Open Sans", sans-serif; font-size: 34px; color: var(--ink);
  }
  .contact-icon { width: 30px; height: 30px; flex: none; }
</style>
</head>
<body>
<div class="canvas">
  <div class="card">
    <svg class="card-art" width="1000" height="572" viewBox="0 0 1000 572">
      <defs>
        <linearGradient id="photoTone" x1="0" y1="0" x2="1" y2="0.6">
          <stop offset="0" stop-color="var(--photo-green)"/>
          <stop offset=".35" stop-color="var(--photo-skin)"/>
          <stop offset=".7" stop-color="#8a7f7a"/>
          <stop offset="1" stop-color="var(--photo-dark)"/>
        </linearGradient>
        <linearGradient id="ringTone" x1="0" y1="0" x2="1" y2="1">
          <stop offset="0" stop-color="#9a9a9a"/>
          <stop offset="1" stop-color="#3a3a3a"/>
        </linearGradient>
        <linearGradient id="doveTone" x1="0" y1="0" x2="0" y2="1">
          <stop offset="0" stop-color="#e6e6e6" stop-opacity=".55"/>
          <stop offset="1" stop-color="#e6e6e6" stop-opacity=".15"/>
        </linearGradient>
      </defs>

      <path class="ornament-top" role="img" aria-label="Grey flourish pattern along the top edge"
            d="M0 0 H1000 V30 H0 Z" fill="var(--ornament)" opacity=".55"/>
      <path class="ornament-right" role="img" aria-label="Grey swirl pattern along the right edge"
            d="M930 0 H1000 V572 H920 C950 420 900 250 930 0 Z" fill="var(--ornament)" opacity=".35"/>
      <path class="ornament-corner" role="img" aria-label="Grey flourish pattern in the lower left corner"
            d="M0 470 H300 L340 572 H0 Z" fill="var(--ornament)" opacity=".8"/>

      <path class="photo" role="img" aria-label="Photograph of a wedding couple with a pink rose bouquet"
            d="M0 30 L360 30 C440 90 480 170 480 260 C480 360 440 430 370 480 L0 480 Z"
            fill="url(#photoTone)"/>
      <path class="photo-frame" d="M360 30 C440 90 480 170 480 260 C480 360 440 430 370 480 L330 572"
            fill="none" stroke="var(--frame)" stroke-width="7"/>

      <path class="dove" role="img" aria-label="Faint white dove illustration"
            d="M570 40 H860 V98 H570 Z" rx="20" fill="url(#doveTone)"/>

      <rect class="rings" role="img" aria-label="Pair of silver wedding rings"
            x="330" y="440" width="170" height="80" rx="40" fill="url(#ringTone)"/>
    </svg>

    <div class="identity">
      <div class="rule"></div>
      <p class="name">Lou Varnik</p>
      <p class="occupation">Marriage Commissioner</p>
      <div class="rule"></div>
    </div>

    <ul class="contacts">
      <li class="contact">
        <svg class="contact-icon" viewBox="0 0 28 28" aria-hidden="true">
          <circle cx="14" cy="14" r="14" fill="var(--icon-bg)"/>
          <path d="M7 11 Q14 6 21 11 L19 13 L17 11.5 L11 11.5 L9 13 Z M9 14 H19 V20 H9 Z" fill="#fff"/>
        </svg>
        <span>780-418-2964</span>
      </li>
      <li class="contact">
        <svg class="contact-icon" viewBox="0 0 28 28" aria-hidden="true">
          <circle cx="14" cy="14" r="14" fill="var(--icon-bg)"/>
          <rect x="7" y="9" width="14" height="10" fill="#fff"/>
          <path d="M7 9 L14 15 L21 9" fill="none" stroke="var(--icon-bg)" stroke-width="1.5"/>
        </svg>
        <span>www.louvarnik.ca</span>
      </li>
      <li class="contact">
        <svg class="contact-icon" viewBox="0 0 28 28" aria-hidden="true">
          <circle cx="14" cy="14" r="14" fill="var(--icon-bg)"/>
          <g fill="none" stroke="#fff" stroke-width="2.2" stroke-linecap="round">
            <path d="M12 16 L16 12"/>
            <path d="M13 10 L15 8 A3 3 0 0 1 20 13 L18 15"/>
            <path d="M15 18 L13 20 A3 3 0 0 1 8 15 L10 13"/>
          </g>
        </svg>
        <span>lou@louvarnik.ca</span>
      </li>
    </ul>
  </div>
</div>
</body>
</html>
```